Brightpath Lending (Mortgage Brokers) needs a Banner Stand design need for trade conference exhibition

We need an eye catching design for a Banner Stand that is 830m (W) x 2000mm (H).

I have created a mock design in PowerPoint but I encourage you to use your creative flair to impress me !

There are several critical non-negotiable requirements as follows :-

Australian Credit Licence 514362 (MUST APPEAR AT BOTTOM),
Green Colour being primary (THIS IS MY CORPORATE COLOUR),
Brightpath Lending Logo (USE ANYONE OF 3 VERSIONS)

In addition I would like the designer to also provide a matching A3 Pull Up Banner Design that is 297mm (W) x 420mm (H) and I have created a PowerPoint mock design with content for that as well.

My target audience is Health Care workers (mostly Doctors), so design needs to relate to that target market.

I have also included some images I use on my website which is www.brightpathlending.com.au in case you want to refer to it.

Finally I have also added a brochure I use which you might want to refer to as well for consistency.

Industry/Entity Type

Trade

```html
<!DOCTYPE html>
<html lang="en">
<head>
<meta charset="utf-8">
<title>Brightpath Lending – Banner Stand</title>
<link rel="stylesheet" href="https://fonts.googleapis.com/css2?family=Lato:wght@400;700;900&family=Open+Sans:ital,wght@1,700;1,800&display=swap">
<style>
  :root {
    --green-light: #9ccf3c;
    --green-mid: #78b82a;
    --green-deep: #5c9e1f;
    --green-dark: #0e5a2b;
    --green-band: #0b4f26;
    --green-fine: #8fcf5a;
    --ink: #1f2d1a;
    --charcoal: #222222;
    --black: #111111;
    --white: #ffffff;
    --photo-light: #f7f7f5;
    --photo-shade: #dcdedd;
  }
  * { margin: 0; padding: 0; box-sizing: border-box; }
  html, body {
    width: 1200px;
    height: 2639px;
    overflow: hidden;
    background: var(--white);
  }
  .banner {
    position: relative;
    width: 1200px;
    height: 2639px;
    overflow: hidden;
    font-family: "Lato", sans-serif;
  }
  .banner-backdrop {
    position: absolute;
    inset: 0;
  }
  .brand-name {
    position: absolute;
    top: 330px;
    left: 560px;
    width: 620px;
    text-align: center;
    font-weight: 400;
    font-size: 66px;
    line-height: 80px;
    color: var(--charcoal);
    letter-spacing: -0.5px;
  }
  .headline {
    position: absolute;
    left: 70px;
    top: 1512px;
    font-family: "Open Sans", sans-serif;
    font-style: italic;
    font-weight: 800;
    font-size: 140px;
    line-height: 142px;
    letter-spacing: -1px;
  }
  .headline-lead { display: block; color: var(--white); }
  .headline-accent { display: block; color: var(--green-dark); }
  .service-list {
    position: absolute;
    left: 70px;
    top: 1846px;
    list-style: none;
  }
  .service-item {
    display: flex;
    align-items: center;
    height: 94px;
    font-weight: 900;
    font-size: 62px;
    color: var(--ink);
  }
  .service-icon {
    width: 60px;
    height: 48px;
    margin-right: 26px;
    flex: none;
  }
  .web-address {
    position: absolute;
    left: 0;
    width: 1200px;
    top: 2448px;
    text-align: center;
    font-weight: 900;
    font-size: 60px;
    line-height: 76px;
    color: var(--white);
  }
  .licence-band {
    position: absolute;
    left: 0;
    bottom: 0;
    width: 1200px;
    height: 106px;
    background: var(--green-band);
    display: flex;
    align-items: center;
    justify-content: center;
    font-size: 30px;
    letter-spacing: 1px;
    color: var(--green-fine);
  }
</style>
</head>
<body>
<main class="banner">
  <svg class="banner-backdrop" width="1200" height="2639" viewBox="0 0 1200 2639" xmlns="http://www.w3.org/2000/svg">
    <defs>
      <linearGradient id="field-green" x1="0" y1="0" x2="1" y2="1">
        <stop offset="0" stop-color="#9ccf3c"/>
        <stop offset="0.55" stop-color="#78b82a"/>
        <stop offset="1" stop-color="#5c9e1f"/>
      </linearGradient>
      <linearGradient id="portrait-tone" x1="0" y1="0" x2="1" y2="1">
        <stop offset="0" stop-color="#f7f7f5"/>
        <stop offset="0.6" stop-color="#f7f7f5"/>
        <stop offset="1" stop-color="#dcdedd"/>
      </linearGradient>
      <clipPath id="white-stage">
        <path d="M1200 1475 C 820 1455, 200 1300, 140 800 C 110 420, 320 120, 500 0 L1200 0 Z"/>
      </clipPath>
    </defs>
    <rect class="green-field" width="1200" height="2639" fill="url(#field-green)"/>
    <path class="swoosh-dark" fill="#0e5a2b" d="M1200 1530 C 800 1510, 80 1340, 65 800 C 50 420, 200 120, 345 0 L1200 0 Z"/>
    <path class="swoosh-black" fill="#111111" d="M1200 1502 C 810 1482, 130 1320, 100 800 C 80 420, 250 120, 415 0 L1200 0 Z"/>
    <path class="swoosh-fine" fill="#78b82a" d="M1200 1487 C 815 1467, 170 1310, 124 800 C 98 420, 290 120, 470 0 L1200 0 Z"/>
    <path class="stage-white" fill="#ffffff" d="M1200 1475 C 820 1455, 200 1300, 140 800 C 110 420, 320 120, 500 0 L1200 0 Z"/>
    <g clip-path="url(#white-stage)">
      <rect class="portrait" role="img" aria-label="Smiling doctor in a white coat with a stethoscope, holding a green apple" x="310" y="560" width="890" height="1000" fill="url(#portrait-tone)"/>
    </g>
  </svg>

  <div class="brand-name">Brightpath Lending</div>

  <h1 class="headline">
    <span class="headline-lead">Is your loan a</span>
    <span class="headline-accent">Bright Loan?</span>
  </h1>

  <ul class="service-list">
    <li class="service-item"><svg class="service-icon" viewBox="0 0 58 46"><path d="M4 42 C 6 18, 26 4, 54 4 C 50 28, 32 42, 4 42 Z" fill="#ffffff"/><path d="M4 42 C 16 30, 30 20, 44 14" stroke="#0e5a2b" stroke-width="5" fill="none"/></svg>Home Loans</li>
    <li class="service-item"><svg class="service-icon" viewBox="0 0 58 46"><path d="M4 42 C 6 18, 26 4, 54 4 C 50 28, 32 42, 4 42 Z" fill="#ffffff"/><path d="M4 42 C 16 30, 30 20, 44 14" stroke="#0e5a2b" stroke-width="5" fill="none"/></svg>Car &amp; Vehicle Loans</li>
    <li class="service-item"><svg class="service-icon" viewBox="0 0 58 46"><path d="M4 42 C 6 18, 26 4, 54 4 C 50 28, 32 42, 4 42 Z" fill="#ffffff"/><path d="M4 42 C 16 30, 30 20, 44 14" stroke="#0e5a2b" stroke-width="5" fill="none"/></svg>Commercial Property</li>
    <li class="service-item"><svg class="service-icon" viewBox="0 0 58 46"><path d="M4 42 C 6 18, 26 4, 54 4 C 50 28, 32 42, 4 42 Z" fill="#ffffff"/><path d="M4 42 C 16 30, 30 20, 44 14" stroke="#0e5a2b" stroke-width="5" fill="none"/></svg>Business Loans</li>
    <li class="service-item"><svg class="service-icon" viewBox="0 0 58 46"><path d="M4 42 C 6 18, 26 4, 54 4 C 50 28, 32 42, 4 42 Z" fill="#ffffff"/><path d="M4 42 C 16 30, 30 20, 44 14" stroke="#0e5a2b" stroke-width="5" fill="none"/></svg>Equipment Finance</li>
    <li class="service-item"><svg class="service-icon" viewBox="0 0 58 46"><path d="M4 42 C 6 18, 26 4, 54 4 C 50 28, 32 42, 4 42 Z" fill="#ffffff"/><path d="M4 42 C 16 30, 30 20, 44 14" stroke="#0e5a2b" stroke-width="5" fill="none"/></svg>SMSF Loans</li>
  </ul>

  <p class="web-address">www.brightpathlending.com.au</p>

  <footer class="licence-band">Australian Credit Licence 514362</footer>
</main>
</body>
</html>
```